Corporate brochure design 4 pages

Hi,

We are a real estate company based in Europe.

We have almost finalized a rebranding.

We are developing a brand book guidelines (still on working process) to help you undertstand the look and feel of our new CI. I would like to receive proposals of design for a corporate brochure template. I need to receive the Indesign files with full ownership rights to be able to adapt all our documentation with this template.
Regarding the images, you can take gabaris on www.pelvaromedia.com. I will be able to take them afterwards.

There will be 4 pages. you will receive the 4 pages on pdf for your consideration with our (almost) actual layout.

- 1st page: cover
- 2nd page: company presentation in french and english
- 3rd page: some market data + graph
- 4th page: 2 retail centers presentation.

In the template, i need to have:
- the paragraph styles in order
- 2 different masters with top/bottom/page number aso.

Please feel free to ask any other questions.

best regards,
Updates

I would like to precise tha t we are active on the commercial real estate sector:

- office transactions (rent /sales)
- property management of administrative and business buildings
- Valuation of properties
- Capital markets (investment advices for selling building)

Industry/Entity Type

Real Estate

Colors

Designer to choose colors to be used in the design.

```html
<!DOCTYPE html>
<html lang="en">
<head>
<meta charset="utf-8">
<title>Meridian – Luxembourg Office Market Report Q3-2013</title>
<link rel="stylesheet" href="https://fonts.googleapis.com/css2?family=Open+Sans:wght@300;400;600;700&display=swap">
<style>
  :root{
    --stage:#5c5c5c;
    --paper:#ffffff;
    --ink:#1a1a1a;
    --black:#0d0d0d;
    --brown:#24140f;
    --orange:#f26a1b;
    --row:#cfcfcf;
    --row-light:#e4e4e4;
    --muted:#6d6d6d;
    --sky-a:#9fc4e4;
    --sky-b:#4d6f8f;
    --stone:#b9ad9c;
  }
  *{box-sizing:border-box;margin:0;padding:0}
  html,body{width:1200px;height:900px;overflow:hidden}
  body{background:var(--stage);font-family:"Open Sans",Arial,sans-serif;color:var(--ink);position:relative}
  .page{position:absolute;width:280px;height:396px;background:var(--paper);overflow:hidden;box-shadow:0 6px 18px rgba(0,0,0,.35)}
  .page svg.bg{position:absolute;inset:0;width:280px;height:396px}
  .page--cover{left:80px;top:40px}
  .page--retail{left:400px;top:40px}
  .page--about{left:560px;top:464px;box-shadow:-2px 6px 18px rgba(0,0,0,.35)}
  .page--market{left:840px;top:464px}
  .abs{position:absolute}

  /* cover */
  .cover-title{right:22px;top:282px;text-align:right;color:#fff;letter-spacing:.04em;line-height:1.25}
  .cover-title .place{font-weight:300;font-size:10px}
  .cover-title .report{font-weight:700;font-size:11px}
  .cover-title .period{font-weight:300;font-size:10px}
  .brand{right:22px;top:334px;text-align:right}
  .brand-name{font-weight:700;font-size:17px;color:#fff;letter-spacing:.03em}
  .brand-line{font-size:5px;color:var(--orange);letter-spacing:.22em;margin-top:1px}

  /* retail page */
  .zone-title{font-size:7px;font-weight:400;line-height:1.3;letter-spacing:.03em;text-transform:uppercase}
  .zone-title--city{left:150px;top:66px}
  .zone-title--station{left:112px;top:282px}
  .retail-table{position:absolute;left:12px;width:256px;border-collapse:separate;border-spacing:0 2px;font-size:4.6px;line-height:1.3}
  .retail-table th{text-align:left;font-weight:600;width:78px;padding:1px 3px;vertical-align:top}
  .retail-table td{background:var(--row);padding:1px 4px}
  .retail-table tr:nth-child(even) td{background:var(--row-light)}
  .retail-table--city{top:100px}
  .retail-table--station{top:196px}

  /* about page */
  .col{width:118px;font-size:4.6px;line-height:1.45;color:var(--muted)}
  .col--fr{left:14px;top:96px}
  .col--en{left:150px;top:64px}
  .kicker{font-size:5px;font-weight:700;color:var(--orange);letter-spacing:.06em;text-transform:uppercase}
  .col h2{font-size:9px;font-weight:400;color:var(--ink);margin:2px 0 5px;letter-spacing:.03em}
  .col p{margin-bottom:4px}
  .team-list{left:8px;top:262px;list-style:none;color:#fff;font-size:4.8px;line-height:2}
  .folio{bottom:5px;font-size:5px;color:#fff}
  .folio--left{left:8px}
  .folio--right{right:8px}

  /* market page */
  .stock-head{top:18px;width:118px}
  .stock-head--fr{left:14px}
  .stock-head--en{left:148px}
  .stock-head .kicker{font-size:4.4px}
  .stock-head h2{font-size:9px;font-weight:400;letter-spacing:.03em;margin-top:1px}
  .stock-head p{font-size:4.2px;line-height:1.4;color:var(--muted);margin-top:3px}
  .stock-table{position:absolute;left:14px;top:68px;width:252px;border-collapse:collapse;font-size:4.3px;line-height:1.5}
  .stock-table th{text-align:left;font-weight:700;color:var(--orange);font-size:4.2px;padding-bottom:2px}
  .stock-table td{padding:0 2px;border-bottom:.5px solid #e3e3e3}
  .stock-table td.zone{font-weight:700;width:82px}
  .stock-table td.num{text-align:right}
  .stock-table tr.total td{font-weight:700;background:#efefef}
  .chart{right:8px;top:280px;width:100px;height:48px}
</style>
</head>
<body>

<!-- Cover -->
<section class="page page--cover">
  <svg class="bg" viewBox="0 0 280 396" aria-hidden="true">
    <defs>
      <linearGradient id="sky" x1="0" y1="0" x2="1" y2="1">
        <stop offset="0" stop-color="var(--sky-a)"/>
        <stop offset=".55" stop-color="var(--stone)"/>
        <stop offset="1" stop-color="var(--sky-b)"/>
      </linearGradient>
    </defs>
    <rect x="0" y="0" width="280" height="280" fill="url(#sky)" role="img" aria-label="Photograph of a glass office facade against a blue sky"/>
    <polygon points="195,0 280,0 280,172 120,223" fill="var(--brown)"/>
    <polygon points="0,262 280,172 280,396 0,396" fill="var(--black)"/>
    <polygon points="0,372 165,350 120,396 0,396" fill="var(--orange)"/>
  </svg>
  <div class="abs cover-title">
    <div class="place">LUXEMBOURG</div>
    <div class="report">OFFICE MARKET REPORT</div>
    <div class="period">Q3-2013</div>
  </div>
  <div class="abs brand">
    <div class="brand-name">MERIDIAN</div>
    <div class="brand-line">COMMERCIAL REAL ESTATE</div>
  </div>
</section>

<!-- Retail centres page -->
<section class="page page--retail">
  <svg class="bg" viewBox="0 0 280 396" aria-hidden="true">
    <defs>
      <linearGradient id="facade" x1="0" y1="0" x2="1" y2="1">
        <stop offset="0" stop-color="var(--sky-a)"/>
        <stop offset="1" stop-color="var(--sky-b)"/>
      </linearGradient>
    </defs>
    <polygon points="110,0 280,0 280,95" fill="url(#facade)" role="img" aria-label="Photograph of an office building facade"/>
    <rect x="10" y="8" width="92" height="56" fill="#e6e6e6" role="img" aria-label="Street map of the Luxembourg city pedestrian zone"/>
    <polygon points="0,262 220,396 0,396" fill="var(--black)"/>
    <polygon points="0,336 112,396 0,396" fill="var(--orange)"/>
    <rect x="196" y="326" width="76" height="58" fill="#e6e6e6" role="img" aria-label="Street map of the station district"/>
  </svg>
  <h2 class="abs zone-title zone-title--city">High Streets<br>Luxembourg-<br>City - Pedestrian Zone</h2>
  <table class="retail-table retail-table--city">
    <tr><th>Localisation</th><td>Pedestrian area: Grand Rue, Rue Philippe II</td></tr>
    <tr><th>Surface totale</th><td>51 500 m² - sqm</td></tr>
    <tr><th>Emplacements</th><td>+/- 400</td></tr>
    <tr><th>Loyers / rents</th><td>960 – 1 320 €/m²/year</td></tr>
    <tr><th>Parking</th><td>2 600 (public)</td></tr>
    <tr><th>Marques principales</th><td>Corvina, Lindqvist, Maison Aubrel, Vessant, Horlogerie Stamm, Orsetta, Kalvo, Brenmoor, Tessaly, Veradin, Ombrelle, Falcaro, Ninove, Sortino, Halvard, Luminet</td></tr>
  </table>
  <table class="retail-table retail-table--station">
    <tr><th>Localisation</th><td>Pedestrian area: Grand Rue, Rue Philippe II</td></tr>
    <tr><th>Surface - Sizes</th><td>51 500 m² - sqm</td></tr>
    <tr><th>Rental levels - Retail bands</th><td>+/- 400</td></tr>
    <tr><th>Loyers / rents excl. VAT</th><td>960 – 1 320</td></tr>
    <tr><th>Parking</th><td>2 600 (public)</td></tr>
    <tr><th>Marques principales - Main brands</th><td>Corvina, Lindqvist, Maison Aubrel, Vessant, Horlogerie Stamm, Orsetta, Kalvo, Brenmoor, Tessaly, Veradin, Ombrelle, Falcaro, Ninove, Sortino, Halvard</td></tr>
  </table>
  <h2 class="abs zone-title zone-title--station">High Streets<br>Luxembourg Station<br>Av. Gare</h2>
</section>

<!-- Company presentation page -->
<section class="page page--about">
  <svg class="bg" viewBox="0 0 280 396" aria-hidden="true">
    <defs>
      <linearGradient id="skyline" x1="0" y1="0" x2="1" y2="0">
        <stop offset="0" stop-color="#2d4f7c"/>
        <stop offset="1" stop-color="#8fb6dc"/>
      </linearGradient>
    </defs>
    <path d="M0 0 H280 V30 Q140 62 0 44 Z" fill="url(#skyline)" role="img" aria-label="Photograph of a business district skyline"/>
    <path d="M0 44 Q140 62 280 30 V38 Q140 70 0 50 Z" fill="#eae6df"/>
    <rect x="70" y="244" width="210" height="130" fill="#8c97a3" role="img" aria-label="Team photograph of four partners in suits"/>
    <polygon points="0,252 76,252 76,352 0,366" fill="var(--black)"/>
    <polygon points="0,366 280,352 280,360 140,396 0,396" fill="var(--orange)"/>
  </svg>
  <div class="abs col col--fr">
    <div class="kicker">À propos de nous</div>
    <h2>UNE ÉQUIPE</h2>
    <p>Proposer des services de qualité répondant parfaitement à vos attentes est notre ambition. Elle est partagée par tous les membres de notre équipe.</p>
    <p>Nos consultants accompagnent propriétaires et locataires à chaque étape de leurs projets immobiliers, de la recherche de bureaux jusqu'à la gestion.</p>
    <p>Notre connaissance du marché luxembourgeois vous garantit un conseil indépendant et durable.</p>
  </div>
  <div class="abs col col--en">
    <div class="kicker">About us</div>
    <h2>A TEAM</h2>
    <p>Our ambition is to offer quality services that perfectly meet your expectations. This ambition is shared by all members of our team.</p>
    <p>Our consultants support owners and tenants at every stage of their property projects, from office search to management.</p>
    <p>Our knowledge of the Luxembourg market ensures independent and lasting advice.</p>
  </div>
  <ul class="abs team-list">
    <li>Luc Ferrand</li>
    <li>Paul Maret</li>
    <li>Eric Dorsel</li>
    <li>Henri Valdor</li>
  </ul>
  <span class="abs folio folio--left">2</span>
</section>

<!-- Market data page -->
<section class="page page--market">
  <svg class="bg" viewBox="0 0 280 396" aria-hidden="true">
    <polygon points="170,0 280,0 280,18 200,10" fill="#6f93b8" role="img" aria-label="Photograph of office towers"/>
    <rect x="80" y="280" width="84" height="54" fill="#b7c2cc" role="img" aria-label="Photograph of a meeting in an office"/>
    <polygon points="0,352 280,336 280,396 0,396" fill="var(--black)"/>
    <polygon points="0,352 110,346 80,366 0,370" fill="var(--orange)"/>
  </svg>
  <div class="abs stock-head stock-head--fr">
    <div class="kicker">Marché de bureaux Luxembourg Q3 2013</div>
    <h2>STOCK</h2>
    <p>Le stock de bureaux est réparti entre le centre-ville, la ville-périphérie et la périphérie.</p>
  </div>
  <div class="abs stock-head stock-head--en">
    <div class="kicker">Luxembourg office market report Q3 2013</div>
    <h2>STOCK</h2>
    <p>The office stock is spread between the city centre, the city periphery and the periphery.</p>
  </div>
  <table class="stock-table">
    <tr><th></th><th>Quartiers / Districts</th><th class="num">Stock m²</th><th class="num">Stock %</th></tr>
    <tr><td class="zone">Centre-ville (City)</td><td>Centre</td><td class="num">456 000</td><td class="num">14,1 %</td></tr>
    <tr><td></td><td>Gare</td><td class="num">190 000</td><td class="num">5,9 %</td></tr>
    <tr><td></td><td>Kirchberg</td><td class="num">742 000</td><td class="num">22,9 %</td></tr>
    <tr><td></td><td>Cloche d'Or</td><td class="num">286 000</td><td class="num">8,8 %</td></tr>
    <tr class="total"><td></td><td>Total</td><td class="num">1 674 000</td><td class="num">51,7 %</td></tr>
    <tr><td class="zone">Ville-périphérie</td><td>Howald</td><td class="num">148 000</td><td class="num">4,6 %</td></tr>
    <tr><td></td><td>Strassen</td><td class="num">176 000</td><td class="num">5,4 %</td></tr>
    <tr class="total"><td></td><td>Total</td><td class="num">324 000</td><td class="num">10,0 %</td></tr>
    <tr><td class="zone">Périphérie</td><td>Nord</td><td class="num">412 000</td><td class="num">12,7 %</td></tr>
    <tr><td></td><td>Sud</td><td class="num">538 000</td><td class="num">16,6 %</td></tr>
    <tr><td></td><td>Aéroport</td><td class="num">290 000</td><td class="num">9,0 %</td></tr>
    <tr class="total"><td></td><td>Total</td><td class="num">3 238 000</td><td class="num">100 %</td></tr>
  </table>
  <svg class="abs chart" viewBox="0 0 100 48" role="img" aria-label="Bar chart of office stock growth">
    <line x1="2" y1="44" x2="98" y2="44" stroke="#bbb" stroke-width=".5"/>
    <g fill="var(--orange)">
      <rect x="4" y="30" width="6" height="14"/>
      <rect x="13" y="28" width="6" height="16"/>
      <rect x="22" y="26" width="6" height="18"/>
      <rect x="31" y="24" width="6" height="20"/>
      <rect x="40" y="21" width="6" height="23"/>
      <rect x="49" y="18" width="6" height="26"/>
      <rect x="58" y="15" width="6" height="29"/>
      <rect x="67" y="12" width="6" height="32"/>
      <rect x="76" y="9" width="6" height="35"/>
      <rect x="85" y="6" width="6" height="38"/>
    </g>
  </svg>
  <span class="abs folio folio--right">3</span>
</section>

</body>
</html>
```